Label for ORGANIC ROSE WATER

Organic Rose Water is a second product from a family of products that we develop. The first product was Organic Argan Oil. The label for this product should be in the same style as the first label that we have. The bottle will be exactly the same. It is good to know that the text should be in GOLD colour (not yellow) it is possible that we continue the same gold or use ROSE (pink) gold. We still have not decided what will suit more.
The fonts that are used in this labels are:
Raleway
and
Butler
both fonts can be found in typemeadow for free
Women and girls.
Cosmetics
- Black label, gold or pink gold colours.
- As this is rose water and the label is minimalistic, the designer should find the best way to input somewhere and somehow rose colour to make the product recognisable.

```html
<!DOCTYPE html>
<html lang="en">
<head>
<meta charset="utf-8">
<title>Velmora Organic Rose Water – Label</title>
<link href="https://fonts.googleapis.com/css2?family=Playfair+Display:wght@500&family=Raleway:wght@300;400;600;700&display=swap" rel="stylesheet">
<style>
  :root{
    --canvas:#ffffff;
    --label-gold:#b8975e;
    --label-gold-deep:#a9874f;
    --ink-light:#fbf4e6;
    --ink-dark:#2a2118;
    --rose:#f6cdd2;
    --rose-deep:#e9a8b3;
    --leaf:#6f8a45;
    --badge-green:#7a9a3c;
    --badge-red:#a8473e;
  }
  *{box-sizing:border-box;margin:0;padding:0}
  html,body{width:710px;height:1200px;overflow:hidden;background:var(--canvas)}
  body{position:relative;font-family:"Raleway",sans-serif;color:var(--ink-light)}

  .label{position:absolute;left:20px;top:57px;width:670px;height:424px;background:var(--label-gold);overflow:hidden}

  .panel{position:absolute;top:0;height:100%}
  .panel--warnings{left:0;width:230px;padding:16px 14px 0 18px}
  .panel--front{left:230px;width:210px}
  .panel--usage{left:440px;width:230px;padding:14px 18px 0 12px}

  .copy{font-size:6.3px;line-height:1.55;font-weight:400;margin-bottom:9px;text-align:justify}
  .copy b{font-weight:700}
  .lang{display:inline-block;background:var(--ink-light);color:var(--label-gold-deep);font-weight:700;font-size:6px;border-radius:3px;padding:0 3px;margin-right:3px}
  .heading{font-size:6.6px;font-weight:700;letter-spacing:.3px;margin:8px 0 4px;text-transform:uppercase}

  .origin{font-size:6.6px;font-weight:700;color:var(--ink-dark);margin-top:4px}
  .maker{font-size:6px;line-height:1.45;margin-top:3px}
  .badges{position:absolute;left:18px;right:14px;bottom:14px;height:60px}
  .blank-box{position:absolute;left:0;bottom:0;width:96px;height:20px;background:#fff}
  .badge{position:absolute}
  .badge--vegan{right:62px;top:0;width:22px;height:22px;border-radius:50%;background:var(--rose-deep)}
  .badge--recycle{right:74px;bottom:0;width:22px;height:18px;border:1px solid var(--ink-dark);border-radius:2px}
  .badge--shelf{right:40px;bottom:0;width:16px;height:18px;border:1px solid var(--ink-dark);border-radius:2px}
  .badge--organic{right:4px;bottom:-2px;width:28px;height:28px;border-radius:50%;background:var(--badge-green);border:2px solid var(--badge-red)}

  .linework{position:absolute;left:20px;top:60px;width:175px;height:290px;border-radius:45% 55% 40% 60%;
    background:radial-gradient(ellipse at center,rgba(232,196,120,.22),rgba(232,196,120,0) 70%)}
  .brand{position:absolute;top:30px;left:0;width:100%;text-align:center;font-family:"Raleway",sans-serif;font-weight:400;font-size:24px;letter-spacing:1px;color:var(--ink-dark)}
  .title{position:absolute;left:0;width:100%;text-align:center;color:var(--rose)}
  .title__organic{top:114px;font-size:14px;letter-spacing:1px;font-weight:300;padding-left:20px}
  .title__rose{top:128px;font-family:"Playfair Display",serif;font-weight:500;font-size:58px;line-height:1;letter-spacing:-1px}
  .title__water{top:194px;font-size:14px;letter-spacing:1px;font-weight:300;padding-left:80px}

  .variant{position:absolute;left:28px;top:232px;font-size:8px;line-height:1.45;font-weight:600}
  .rule{position:absolute;left:28px;top:262px;width:18px;height:1px;background:var(--ink-light)}
  .claim{position:absolute;left:28px;top:268px;font-size:8px;line-height:1.45;font-weight:300;color:#f0e3c6}
  .rose-art{position:absolute;left:100px;top:310px;width:95px;height:80px;border-radius:50% 45% 50% 40%;
    background:radial-gradient(circle at 40% 60%,var(--rose) 0 38%,var(--rose-deep) 55%,rgba(111,138,69,.7) 75%,rgba(111,138,69,0) 85%)}
  .volume{position:absolute;left:28px;top:372px;font-size:7px;line-height:1.3;color:var(--ink-dark)}
</style>
</head>
<body>
  <section class="label">

    <div class="panel panel--warnings">
      <p class="copy"><span class="lang">EN</span><b>CAUTION:</b> For external use only. Store in a cool place. Avoid contact with eyes. Keep out of the reach of children. If pregnant, consult with your health care provider before use. Rub a very small amount on the inside of your elbow area to test for any allergic reaction before use. 100% of the total ingredients are from Organic Farming.</p>
      <p class="copy"><span class="lang">DE</span><b>VORSICHT:</b> Nur zur äußerlichen Anwendung. Kühl lagern. Vermeiden Sie den Kontakt mit den Augen. Halten Sie es außerhalb der Reichweite von Kindern. Wenn Sie schwanger sind, wenden Sie sich vor der Anwendung an Ihren Arzt. Reiben Sie eine sehr kleine Menge auf die Innenseite Ihres Ellenbogenbereichs, um vor der Anwendung auf allergische Reaktionen zu testen. 100% der gesamten Inhaltsstoffe stammen aus biologischem Anbau.</p>
      <p class="copy"><span class="lang">FR</span><b>ATTENTION:</b> Pour usage externe seulement. Conserver dans un endroit frais. Éviter le contact avec les yeux. Garder hors de la portée des enfants. Si vous êtes enceinte, consultez votre professionnel de la santé avant d'utiliser ce produit. Frotter une très petite quantité à l'intérieur du coude pour vérifier s'il y a une réaction allergique avant l'utilisation. 100% du total des ingrédients sont issus de l'Agriculture Biologique.</p>
      <p class="origin">Imported from Agadir, Morocco</p>
      <p class="maker">Manufactured for<br>Maren Studio Ltd<br>Linden Row Trading<br>Plovdiv, Bulgaria</p>
      <div class="badges">
        <div class="badge badge--vegan"></div>
        <div class="badge badge--recycle"></div>
        <div class="badge badge--shelf"></div>
        <div class="badge badge--organic"></div>
        <div class="blank-box"></div>
      </div>
    </div>

    <div class="panel panel--front">
      <div class="linework" role="img" aria-label="Fine gold line-art drawing of a flowing rose outline"></div>
      <p class="brand">Velmora</p>
      <p class="title title__organic">ORGANIC</p>
      <p class="title title__rose">Rose</p>
      <p class="title title__water">WATER</p>
      <p class="variant">BIO Rosenwasser<br>Eau de Rose BIO</p>
      <span class="rule"></span>
      <p class="claim">100% Pure and Natural<br>Rosa Damascena</p>
      <div class="rose-art" role="img" aria-label="Illustration of two pale pink roses with green leaves"></div>
      <p class="volume">100ml ℮<br>3.38 fl oz</p>
    </div>

    <div class="panel panel--usage">
      <p class="copy"><b>Ingredients:</b> Rosa Damascena Flower Water*<br>* certified organic ingredient</p>
      <p class="heading"><span class="lang">EN</span>How to use</p>
      <p class="copy"><b>Hair:</b> Mist onto hair 20 minutes before shampooing. Apply a few sprays as often as needed to achieve soft, shiny hair. Can be added to shampoo.<br><b>Skin:</b> Apply 2-3 sprays to clean face in the morning or as a gentle toner.<br><b>Nail:</b> Massage onto your nails, cuticles and the skin surrounding your nails.</p>
      <p class="heading"><span class="lang">DE</span>Wie man es benutzt</p>
      <p class="copy"><b>Haar:</b> Ins ganze Haar für 20 Minuten einmassieren vor waschen. Tragen Sie einige Tropfen so oft wie nötig auf, um weiches, glänzendes Haar zu erhalten. Kann dem Shampoo hinzugefügt werden.<br><b>Haut:</b> Tragen Sie 2-3 Sprühstöße morgens auf das Gesicht auf.<br><b>Nagel:</b> Massieren Sie es auf Ihre Nägel, Nagelhaut und auf die Haut um Ihre Nägel herum.</p>
      <p class="heading"><span class="lang">FR</span>Comment l'utiliser</p>
      <p class="copy"><b>Cheveux:</b> Masser dans les cheveux pendant 20 minutes avant le shampooing. Appliquer quelques gouttes aussi souvent que nécessaire pour obtenir des cheveux doux et brillants. Peut être ajouté au shampooing.<br><b>Peau:</b> Vaporiser 2-3 fois sur le visage propre le matin comme un tonique.<br><b>Ongles:</b> Masser sur vos ongles, vos cuticules et la peau autour de vos ongles.</p>
    </div>

  </section>
</body>
</html>
```